PowerPoint Design Project

Powerpoint design for an online marketing agency.
PP will be used as a WhitePaper to showcase our expertise.
Our USP is that we use data for marketing so the design must reflect this with charts and graphs.
A set of images is available in our flickr account
http://www.pixelvault.example/photos/kelmora/sets/48302916574021983/with/3104827561/
We already have written real content for the PP for you to work with.
Updates

1. I have added a sample of the content a 2-page extract in a word document. The full document is around 15 pages.
2. While the finished piece is to be in PowerPoint format, it will also be used as a White Paper so the design should reflect this - i.e it should be able to be read like it was a well designed Word document not just a PP
3. The design you see in the sample 2-page document is just for illustration purposes it is not intended to influence the final design at all. So for example it currently has some pull-quotes in black boxes - that is just to show what they are and I don't want the final piece to have black boxes around quotes.
4. I've been asked to make this project guaranteed: as this is the first time I've used ArtHivePro I'm going to keep it as a standard project but we are committed to the work.
5. The current deadline is for the START of design work. We need the completed design by 21 September, so there is plenty of time to schedule this in with your other work.
Many thanks
Nigel 

The designs shown so far would not be suitable for turning into a WhitePaper. For example the bars across the top of the design create a break at the start of each page rather than emphasise the continuous nature of the document. 

Here is an example of some great design for a similar project - and we've uploaded another sample as a file

http://www.surgeloft.example/downloads/[SURGE]-what-its-like-working-

If you asked me for some ideas on the feel of the design I would say:

1. Bold - it has to look interesting - corporate world but it doesn't need to feel dull/grey
2. Exciting 
3. Precise - easy to read , not a fussy design

Target Market(s)

Business developers, sales managers, CEOs of companies with over 5 employees but without their own marketing department

Industry/Entity Type

Marketing

Requirements
Must have
• Flawless design that says "this company is smart and means business"
Nice to have
• the powerpoint should lend itself to easy file/saveas to be delivered as a PDF and for individual slides to be extracted for presentation, or use as images in blog posts etc (so for example any page number must be easy to remove).
Should not have
• no cartoons, no line drawings, nothing to obscure easy legibility

```html
<!DOCTYPE html>
<html lang="en">
<head>
<meta charset="utf-8">
<title>The Science of Marketing – kelmora White Paper</title>
<link rel="stylesheet" href="https://fonts.googleapis.com/css2?family=Tinos:ital,wght@0,400;0,700;1,400&family=Arimo:wght@400;700&display=swap">
<style>
  :root {
    --page: #ffffff;
    --ink: #1a1a1a;
    --quote-ink: #1f2f57;
    --quote-bg-top: #eef1f7;
    --quote-bg-bottom: #d3dae8;
    --frame: #c9ced8;
    --grid: #e3e6ec;
    --callout: #2a6fc9;
    --bar-blue: #3f6fb5;
    --bar-red: #b8453f;
    --bar-teal: #3a9fb8;
    --bar-orange: #e8893a;
    --bar-sky: #8ba7d8;
    --bar-green: #93b451;
    --bar-purple: #7b619e;
    --footer: #333333;
  }
  * { box-sizing: border-box; margin: 0; padding: 0; }
  html, body { width: 900px; height: 1200px; overflow: hidden; background: var(--page); }
  .page {
    position: relative;
    width: 900px; height: 1200px;
    font-family: "Tinos", "Times New Roman", serif;
    color: var(--ink);
  }
  .intro {
    position: absolute; left: 126px; top: 14px; width: 660px;
    font-size: 22px; line-height: 32px;
  }
  .intro sup { font-size: 13px; line-height: 0; }
  .benefits { list-style: none; }
  .benefits li { position: relative; padding-left: 40px; }
  .benefits li::before {
    content: ""; position: absolute; left: 6px; top: 12px;
    width: 8px; height: 8px; border-radius: 50%; background: var(--ink);
  }
  .word-chart {
    position: absolute; left: 132px; top: 352px; width: 648px; height: 388px;
    border: 1px solid var(--frame);
    box-shadow: 3px 4px 8px rgba(0,0,0,0.18);
    background: var(--page);
  }
  .word-chart svg { display: block; }
  .chart-callout {
    position: absolute; left: 362px; top: 16px; width: 262px;
    background: var(--callout); color: #fff;
    font-family: "Arimo", Arial, sans-serif;
    font-size: 11px; line-height: 14px; padding: 8px 12px;
  }
  .chart-callout ul { list-style: none; margin: 5px 0; }
  .chart-callout li::before { content: "- "; }
  .chart-callout .source { font-size: 8px; line-height: 10px; }
  .summary {
    position: absolute; left: 126px; top: 750px; width: 660px;
    font-size: 24px; line-height: 34px;
  }
  .pull-quote {
    position: absolute; left: 156px; top: 836px; width: 630px; height: 82px;
    background: linear-gradient(to bottom, var(--quote-bg-top), var(--quote-bg-bottom));
    box-shadow: 2px 3px 6px rgba(0,0,0,0.25);
    font-style: italic; color: var(--quote-ink);
    font-size: 19px; line-height: 24px; padding: 14px 20px 0 18px;
  }
  .pull-quote .mark { font-size: 26px; vertical-align: -3px; }
  .closing {
    position: absolute; left: 126px; top: 942px; width: 660px;
    font-size: 22px; line-height: 34px;
  }
  .page-footer {
    position: absolute; left: 12px; right: 12px; top: 1172px;
    display: flex; justify-content: space-between;
    font-family: "Arimo", Arial, sans-serif; font-size: 11px; color: var(--footer);
  }
</style>
</head>
<body>
<main class="page">
  <section class="intro">
    <p>Combining marketing expertise, statistical data, and psychological research from behavioural economics, the science of marketing explains how companies can use 21<sup>st</sup> century marketing strategies like blogging, social media and permission-based email marketing to:</p>
    <ul class="benefits">
      <li>know what works in marketing, based on interpreting measurable statistical data</li>
      <li>target marketing budgets for highest impact using evidence of return on investment</li>
      <li>adapt marketing campaigns in real-time based on actual customer behaviour.</li>
    </ul>
  </section>

  <figure class="word-chart">
    <svg width="646" height="386" viewBox="0 0 646 386" role="img" aria-label="Bar chart of the most popular words for attracting views">
      <g stroke="var(--grid)" stroke-width="1">
        <line x1="50" y1="36" x2="620" y2="36"/>
        <line x1="50" y1="98" x2="620" y2="98"/>
        <line x1="50" y1="160" x2="620" y2="160"/>
        <line x1="50" y1="222" x2="620" y2="222"/>
        <line x1="50" y1="284" x2="620" y2="284"/>
      </g>
      <line x1="50" y1="346" x2="620" y2="346" stroke="#999" stroke-width="1"/>
      <line x1="50" y1="36" x2="50" y2="346" stroke="#999" stroke-width="1"/>
      <g font-family="Arimo, Arial, sans-serif" font-size="9" fill="#555" text-anchor="end">
        <text x="44" y="39">1000</text><text x="44" y="101">800</text>
        <text x="44" y="163">600</text><text x="44" y="225">400</text>
        <text x="44" y="287">200</text><text x="44" y="349">0</text>
      </g>
      <g>
        <rect x="62" y="55" width="32" height="291" fill="var(--bar-blue)"/>
        <rect x="118" y="98" width="32" height="248" fill="var(--bar-red)"/>
        <rect x="174" y="239" width="32" height="107" fill="var(--bar-teal)"/>
        <rect x="230" y="239" width="32" height="107" fill="var(--bar-teal)"/>
        <rect x="286" y="241" width="32" height="105" fill="var(--bar-teal)"/>
        <rect x="342" y="256" width="32" height="90" fill="var(--bar-orange)"/>
        <rect x="398" y="285" width="32" height="61" fill="var(--bar-sky)"/>
        <rect x="454" y="285" width="32" height="61" fill="var(--bar-sky)"/>
        <rect x="510" y="320" width="32" height="26" fill="var(--bar-green)"/>
        <rect x="566" y="329" width="32" height="17" fill="var(--bar-purple)"/>
      </g>
      <g font-family="Arimo, Arial, sans-serif" font-size="9" fill="#444" text-anchor="middle">
        <text x="78" y="362">insights</text><text x="134" y="362">analysis</text>
        <text x="190" y="362">answers</text><text x="246" y="362">questions</text>
        <text x="302" y="362">advice</text><text x="358" y="362">review</text>
        <text x="414" y="362">why</text><text x="470" y="362">product</text>
        <text x="526" y="362">tips</text><text x="582" y="362">book</text>
      </g>
    </svg>
    <figcaption class="chart-callout">
      The most popular words for attracting views to social media content like blogs or calls to action, imply “thought leadership” including phrases like:
      <ul><li>insights</li><li>analysis</li><li>answers</li><li>questions.</li></ul>
      <p class="source">Source: @danvellari, http://www.quorvanta.example/the-science-of-blogging</p>
    </figcaption>
  </figure>

  <p class="summary">The science of marketing gives you the research and tools to deliver scientific marketing that works, based on data you can prove.</p>

  <blockquote class="pull-quote"><span class="mark">“</span>No longer are size and budget the deciding factors. Now speed and agility are decisive competitive advantage – Daniel Marsh Conway</blockquote>

  <p class="closing">Now you know what the science of marketing is, how can you design a marketing campaign that (to use an Americanism) rocks your ROI?</p>

  <footer class="page-footer">
    <span>©2012 kelmora and or its affiliates. All Rights Reserved.</span>
    <span>kelmora Confidential</span>
  </footer>
</main>
</body>
</html>
```